Breezy Burro Menu Design for new restaurant

Need a menu design for new restaurant- Fast Casual Taqueria. I have the files for our logo and menu already completed. Let me know what type of file your require and I can send it with regard to my logo. I want it to be easy to read but on a half page rack size type card, front and back. Simple and to the point but important to include the items listed with ingredients. Feel free to use icons for different categories.

Target Market(s)

Any one who loves tacos and margaritas...fun...festive...casual...

Font styles to use
Other font styles liked:
• lobster 1.3 and farmer round

Colors
3276b5
ec1f27
ffffff
85cae6
9bcb3c
fbed22

Requirements
Must have
• Designed for a half page, front and back (4.25 x 11). NO full size page menu. Easy to read. Not complicated. Use our logo. I need to be able to modify the menu from my end with out any special software.
Nice to have
• Fun~Festive~ color. Stick with our logo theme using our font lobster 1.3 and farmer round.
Should not have
• Full page format. Do not want stock food phots. Just graphics or icons.

```html
<!DOCTYPE html>
<html lang="en">
<head>
<meta charset="utf-8">
<title>Breezy Burro Menu</title>
<link href="https://fonts.googleapis.com/css2?family=Bebas+Neue&family=Lobster&family=Oswald:wght@500;600&family=Pathway+Gothic+One&display=swap" rel="stylesheet">
<style>
:root{
  --page:#ececec;
  --paper:#ffffff;
  --navy:#2c3a4d;
  --red:#e8434a;
  --sky:#6cbfe0;
  --sky-soft:#cbe7f3;
  --muted:#93adc2;
  --light:#e8eef3;
  --script:"Lobster",cursive;
  --title:"Bebas Neue",sans-serif;
  --num:"Oswald",sans-serif;
  --body:"Pathway Gothic One",sans-serif;
}
*{margin:0;padding:0;box-sizing:border-box}
html,body{width:1056px;height:1200px;overflow:hidden;background:var(--page)}
.canvas{position:relative;width:1056px;height:1200px}
.card{position:absolute;top:72px;width:409px;height:1055px;background:var(--paper);box-shadow:3px 4px 6px rgba(0,0,0,.22);overflow:hidden}
.card--front{left:99px}
.card--back{left:547px}
.script{font-family:var(--script);color:var(--red);font-weight:400}

.item{position:absolute;color:var(--navy)}
.item__name{display:flex;align-items:center;font-family:var(--title);text-transform:uppercase;letter-spacing:.3px;white-space:nowrap}
.item__price{font-family:var(--num);font-weight:600;margin-left:.55em;font-size:.8em;letter-spacing:0}
.item__desc{font-family:var(--body);text-transform:uppercase}

.front .item{left:72px;width:268px}
.front .item__name{font-size:21px;line-height:24px;padding-left:12px;height:24px}
.front .item__desc{font-size:15px;line-height:20px;margin-top:2px}
.front .note{font-size:12.5px;line-height:16px;margin-top:0}

.icon{display:inline-block;background:var(--sky-soft);border-radius:50%;flex:none}
.icon--abs{position:absolute}
.icon--after{margin-left:8px}

.headline{position:absolute;left:70px;top:50px;font-size:34px;line-height:30px;transform:rotate(-2deg);white-space:nowrap}
.headline span{display:block;padding-left:32px}

.band{position:absolute;left:0;right:0;bottom:0;background:var(--navy)}
.band::before{content:"";position:absolute;left:0;right:0;top:-4px;height:8px;
  background:radial-gradient(circle at 4px 4px,var(--paper) 2.6px,transparent 3px) 0 0/8.2px 8px repeat-x}
.band--front{height:134px}
.brand{position:absolute;left:62px;top:46px;font-family:var(--script);font-size:30px;line-height:36px;color:var(--red);display:flex;align-items:center;gap:8px}
.brand__dot{width:14px;height:14px;border-radius:50%;background:var(--sky)}
.social{position:absolute;left:262px;font-family:var(--body);font-size:16px;line-height:18px;color:var(--red);display:flex;align-items:center;gap:6px}
.social__mark{width:14px;height:14px;border-radius:3px;background:var(--sky)}

.tacos-title{position:absolute;left:194px;top:36px;font-family:var(--script);color:var(--navy);font-size:38px;line-height:42px;font-weight:400}
.tacos-icon{left:139px;top:44px;width:43px;height:26px;border-radius:22px 22px 6px 6px}
.tacos-note{position:absolute;left:0;right:0;top:79px;text-align:center;font-family:var(--body);color:var(--red);font-size:12.5px;line-height:16px}

.back .item__name{font-size:18px;line-height:21px;padding-left:12px}
.back .item__desc{font-size:13px;line-height:16px;width:162px;margin-top:2px}
.col1{left:39px}
.col2{left:214px}

.bowl-box{position:absolute;left:213px;top:357px;width:177px;height:401px;border:1.5px solid var(--red)}
.bowl-box::after{content:"";position:absolute;inset:4px;border:1.5px solid var(--red)}
.bowl-title{position:absolute;left:26px;top:60px;font-family:var(--script);color:var(--navy);font-size:31px;line-height:26px}
.bowl-icon{left:112px;top:58px;width:36px;height:80px;border-radius:18px}
.bowl-note{position:absolute;left:20px;right:24px;top:144px;font-family:var(--body);color:var(--red);font-size:10.5px;line-height:12px;text-align:right;text-transform:uppercase;white-space:nowrap}
.bowl-box .item{left:8px;width:150px}
.bowl-box .item__desc{width:140px;font-size:12.5px;line-height:15px;padding-left:12px;padding-left:12px}
.bowl-box .item__desc{margin-left:0}

.band--drinks{height:273px}
.drinks-title{position:absolute;left:25px;top:40px;font-size:34px;line-height:40px}
.drink{position:absolute;display:flex;align-items:baseline;white-space:nowrap;color:var(--sky);font-family:var(--title);font-size:18px;line-height:20px}
.drink small{font-family:var(--body);font-size:11px;color:var(--muted);margin-right:5px;text-transform:uppercase}
.drink .price{font-family:var(--num);font-weight:500;color:var(--light);font-size:14px;margin-left:5px}
.drink .sep{color:var(--sky);margin:0 3px 0 5px;font-size:16px}
.drink .meta{font-family:var(--body);font-size:11px;color:var(--muted);text-transform:uppercase;margin-left:4px}
.drink .meta--bold{font-family:var(--title);font-size:12px;color:var(--sky)}
</style>
</head>
<body>
<div class="canvas">

  <section class="card card--front front">
    <h1 class="headline script">Let's get this party <span>started...</span></h1>

    <div class="item" style="top:141px">
      <div class="item__name">Mexican Poke<span class="item__price">10.50</span><span class="icon icon--after" role="img" aria-label="fish tail icon" style="width:22px;height:32px;margin-top:-14px"></span></div>
      <div class="item__desc">Fresh ahi tuna blended w/ spices &amp; ponzu on a bed of colored cabbage</div>
    </div>

    <span class="icon icon--abs" role="img" aria-label="shrimp icon" style="left:58px;top:214px;width:20px;height:30px"></span>
    <div class="item" style="top:220px">
      <div class="item__name">Mermaid Tails<span class="item__price">10.50</span></div>
      <div class="item__desc">Shrimp tempura beached on coconut slaw w/ sweet heat glaze, rice pearls, fresh cilantro</div>
    </div>

    <div class="item" style="top:299px">
      <div class="item__name">Fiesta Nachos<span class="item__price">10.50</span><span class="icon icon--after" role="img" aria-label="nacho chips icon" style="width:36px;height:24px;border-radius:6px;margin-top:-6px"></span></div>
      <div class="item__desc">Crunchy tortilla chips layered w/ queso fresco, pickled vegetables, black beans, tomatillo salsa, dry chile salsa &amp; cilantro. As flavorful as it is colorful!</div>
      <div class="item__desc note">*Add any protein for upcharge</div>
    </div>

    <div class="item" style="top:430px">
      <div class="item__name">Chorizo &amp; Queso<span class="item__price">10.50</span></div>
      <div class="item__desc">Melted queso fresco w/ chorizo crumbles, caramelized onions, cilantro</div>
    </div>

    <span class="icon icon--abs" role="img" aria-label="corn icon" style="left:61px;top:506px;width:19px;height:26px"></span>
    <div class="item" style="top:509px">
      <div class="item__name">Elote<span class="item__price">10.50</span></div>
      <div class="item__desc">Roasted corn sliced from the cob, chopped onions and poblano peppers w/ cotija cheese, smoky homemade morita mayo &amp; chilera</div>
    </div>

    <div class="item" style="top:608px">
      <div class="item__name">Guacamole &amp; Chips<span class="item__price">10.50</span><span class="icon icon--after" role="img" aria-label="avocado icon" style="width:20px;height:30px;margin-top:-12px"></span></div>
      <div class="item__desc">Smooth blend of Haas avocados, jalapeño, red onions</div>
    </div>

    <div class="item" style="top:687px">
      <div class="item__name">Chips and Salsa<span class="item__price">10.50</span></div>
      <div class="item__desc" style="width:234px">Tortilla chips w/ choice of traditional rojo salsa or tomatillo verde</div>
    </div>
    <span class="icon icon--abs" role="img" aria-label="chips and salsa bowl icon" style="left:308px;top:696px;width:34px;height:38px;border-radius:8px"></span>

    <div class="item" style="top:767px">
      <div class="item__name">Queso and Chips<span class="item__price">10.50</span></div>
      <div class="item__desc">Melted queso fresco &amp; crunchy tortilla chips</div>
    </div>

    <span class="icon icon--abs" role="img" aria-label="rice bowl icon" style="left:50px;top:827px;width:28px;height:20px;border-radius:14px 14px 4px 4px"></span>
    <div class="item" style="top:826px">
      <div class="item__name">Rice &amp; Black Beans<span class="item__price">10.50</span></div>
      <div class="item__desc">Traditional Mexican arroz verde &amp; black beans seasoned w/ epazote</div>
    </div>

    <footer class="band band--front">
      <div class="brand"><span class="brand__dot"></span>Breezy Burro</div>
      <div class="social" style="top:45px"><span class="social__mark"></span>/loremipsum</div>
      <div class="social" style="top:71px"><span class="social__mark"></span>@loremipsum</div>
    </footer>
  </section>

  <section class="card card--back back">
    <span class="icon icon--abs tacos-icon" role="img" aria-label="taco icon"></span>
    <h2 class="tacos-title">Tacos</h2>
    <p class="tacos-note">All tacos finished Breezy Style with fresh cilantro, side of dry chile salsa &amp; lime wedges</p>

    <div class="item col1" style="top:118px"><div class="item__name">Korean<span class="item__price">10.50</span></div>
      <div class="item__desc">Braised short ribs, caramelized onions, cucumber salad, gochujang sauce</div></div>
    <div class="item col1" style="top:198px"><div class="item__name">Barbacoa<span class="item__price">10.50</span></div>
      <div class="item__desc">Spiced angus beef, cool creama, white diced onion, tomatillo-avocado salsa</div></div>
    <div class="item col1" style="top:278px"><div class="item__name">Al Pastor<span class="item__price">10.50</span></div>
      <div class="item__desc">Spit-grilled heritage pork, diced white onion, charred pineapple, queso fresco</div></div>
    <div class="item col1" style="top:358px"><div class="item__name">Carnitas<span class="item__price">10.50</span></div>
      <div class="item__desc">Slow simmered heritage pork, avocado smash, pickled red onion, blistered shishito peppers</div></div>
    <div class="item col1" style="top:438px"><div class="item__name">Alabama Slamma<span class="item__price">10.50</span></div>
      <div class="item__desc">Pulled smoked chicken, Alabama white sauce, pickled cabbage, fried onions, bacon blanket</div></div>
    <div class="item col1" style="top:518px"><div class="item__name">Chick Next Door<span class="item__price">10.50</span></div>
      <div class="item__desc">Grilled chicken breast, elote, avocado smash, queso fresco, salsa verde</div></div>
    <div class="item col1" style="top:597px"><div class="item__name">Yinzer<span class="item__price">10.50</span></div>
      <div class="item__desc">Grilled flat iron steak w/ peppers &amp; onions, melted queso fresco, house jalapeño salsa, chicharrónes</div></div>
    <div class="item col1" style="top:693px"><div class="item__name">Beach Bum<span class="item__price">10.50</span></div>
      <div class="item__desc">Maple fire roasted sweet potato, seasoned black beans, tropical slaw, toasted coconut</div></div>

    <div class="item col2" style="top:118px"><div class="item__name">Island Time<span class="item__price">10.50</span></div>
      <div class="item__desc">Battered avocado, sweet teriyaki glaze, charred pineapple, pickled red onion, queso fresco</div></div>
    <div class="item col2" style="top:198px"><div class="item__name">Tropical Shrimp<span class="item__price">10.50</span></div>
      <div class="item__desc">Shrimp tempura, avocado smash, tropical slaw, sweet heat creama, toasted coconut</div></div>
    <div class="item col2" style="top:278px"><div class="item__name">Cabo Fish<span class="item__price">10.50</span></div>
      <div class="item__desc">Beer battered cod, pickled cabbage, spicy escabeche and smoky homemade morita mayo</div></div>

    <aside class="bowl-box">
      <div class="bowl-title">Bowl<br>me<br>over!!</div>
      <span class="icon icon--abs bowl-icon" role="img" aria-label="taco dropping into bowl icon"></span>
      <div class="bowl-note">Make any Burro taco into a bowl<br>[ gluten free ]</div>
      <div class="item" style="top:198px"><div class="item__name">Ensalada<span class="item__price">10.50</span></div>
        <div class="item__desc">Chopped field greens, black beans, elote, avocado smash, fresh cilantro &amp; queso fresco</div></div>
      <div class="item" style="top:289px"><div class="item__name">Rice &amp; Beans<span class="item__price">10.50</span></div>
        <div class="item__desc">Traditional Mexican arroz verde, seasoned black beans &amp; queso fresco</div></div>
    </aside>

    <footer class="band band--drinks">
      <h2 class="drinks-title script">Drinks</h2>
      <div class="drink" style="left:22px;top:99px"><small>20 oz</small>Tea</div>
      <div class="drink" style="left:22px;top:124px"><small>20 oz</small>Soda Fountain</div>
      <div class="drink" style="left:22px;top:150px">Bottle Soda<span class="meta">see selection</span></div>

      <div class="drink" style="left:171px;top:49px"><small>16 oz</small>Draft Beer<span class="price">7.00</span><span class="sep">/</span><span class="meta" style="margin:0">pitcher</span><span class="price">15.00</span></div>
      <div class="drink" style="left:171px;top:75px">Bottle Beer<span class="meta meta--bold">import/domestic</span><span class="meta">see selection</span></div>
      <div class="drink" style="left:171px;top:100px"><small>16 oz</small>FZ Margarita<span class="price">7.00</span><span class="sep">/</span><span class="meta" style="margin:0">pitcher</span><span class="price">15.00</span></div>
      <div class="drink" style="left:171px;top:126px"><small>16 oz</small>Tap Margarita<span class="price">7.00</span><span class="sep">/</span><span class="meta" style="margin:0">pitcher</span><span class="price">15.00</span></div>
      <div class="drink" style="left:171px;top:151px"><small>16 oz</small>Sangria<span class="price">7.00</span><span class="sep">/</span><span class="meta" style="margin:0">pitcher</span><span class="price">15.00</span></div>
      <div class="drink" style="left:197px;top:176px">Tequila<span class="meta">cheap / standard / premium</span></div>
      <div class="drink" style="left:196px;top:197px"><small>single shot</small><span class="price">7.00</span><span class="sep">/</span><span class="price">7.00</span><span class="sep">/</span><span class="price">7.00</span></div>
      <div class="drink" style="left:192px;top:214px"><small>double shot</small><span class="price">7.00</span><span class="sep">/</span><span class="price">7.00</span><span class="sep">/</span><span class="price">7.00</span></div>
    </footer>
  </section>

</div>
</body>
</html>
```